Insurance company needs a business card design

We need a business card design for a Massachusetts-based insurance company Veloria Insurance, LLC. We provide auto insurance to Hispanic (Spanish- or Portuguese-speaking) immigrants in the United States. We will give these business cards to auto dealers where such customers typically go to purchase vehicles. We will provide a solution to the dealers to provide easy insurance to the customers buying cars at their dealerships. Veloria is the Spanish word for protection.
Contact Information for Business Card
Name, Designation, Company Name, Address, Phone Number, Email, Website
Look and feel
Each slider illustrates characteristics of the customer's brand and the style your logo design should communicate.

```html
<!DOCTYPE html>
<html lang="en">
<head>
<meta charset="utf-8">
<title>Veloria Insurance – Business Card</title>
<link href="https://fonts.googleapis.com/css2?family=Montserrat:wght@400;500;700;800&display=swap" rel="stylesheet">
<style>
  :root{
    --page:#2a2a2b;
    --card:#1a1a1b;
    --card-shade:#202021;
    --orange:#f28a00;
    --blue:#0a528a;
    --white:#f2f2f2;
  }
  *{margin:0;padding:0;box-sizing:border-box}
  html,body{width:1200px;height:881px;overflow:hidden;background:var(--page)}
  body{font-family:'Montserrat',sans-serif;position:relative}
  .card{
    position:absolute;width:560px;height:320px;border-radius:10px;
    background:var(--card);overflow:hidden;
    box-shadow:0 12px 30px rgba(0,0,0,.45);
  }
  .card-back{left:320px;top:90px}
  .card-front{left:320px;top:470px}

  /* back */
  .back-panel{position:absolute;left:0;top:0;width:230px;height:100%;background:var(--card-shade)}
  .brand{
    position:absolute;left:270px;top:140px;display:flex;align-items:center;gap:14px;
  }
  .brand-mark{width:26px;height:26px;background:var(--orange)}
  .brand-name{font-weight:800;font-size:26px;letter-spacing:1px;color:var(--blue);text-transform:uppercase;line-height:1}

  /* front */
  .person{position:absolute;left:36px;top:44px}
  .person-name{font-weight:800;font-size:26px;color:var(--orange);letter-spacing:.5px;text-transform:uppercase}
  .person-title{font-weight:500;font-size:13px;color:var(--white);letter-spacing:1.5px;margin-top:2px}
  .divider{width:20px;height:2px;background:var(--blue);margin:16px 0 14px}
  .address{font-size:13px;color:var(--white);line-height:1.5;letter-spacing:.4px}
  .contact-list{list-style:none;font-size:13px;color:var(--white);letter-spacing:.4px}
  .contact-list li{display:flex;align-items:center;gap:9px;line-height:1.65}
  .contact-list svg{width:11px;height:11px;flex:none}
  .feature-block{position:absolute;right:44px;top:36px;width:170px;height:170px;background:var(--blue)}
  .band-orange{position:absolute;right:0;bottom:38px;width:170px;height:8px;background:var(--orange)}
  .band-blue{position:absolute;left:0;bottom:0;width:100%;height:14px;background:var(--blue)}
</style>
</head>
<body>

<section class="card card-back" aria-label="Card back">
  <div class="back-panel"></div>
  <div class="brand">
    <span class="brand-mark"></span>
    <span class="brand-name">Veloria Insurance</span>
  </div>
</section>

<section class="card card-front" aria-label="Card front">
  <div class="person">
    <h1 class="person-name">Daniel Reyes</h1>
    <p class="person-title">PRESIDENT</p>
    <div class="divider"></div>
    <p class="address">2816 Harbor Lane<br>Fall River, MA 02721</p>
    <div class="divider"></div>
    <ul class="contact-list">
      <li><svg viewBox="0 0 12 12"><path d="M3 1l2 2.5-1.2 1.2c.6 1.4 1.6 2.4 3 3L8 6.5 10.5 8.5 9.5 10.5C5 10.5 1.5 7 1.5 2.5z" fill="var(--orange)"/></svg>508-555-0147</li>
      <li><svg viewBox="0 0 12 12"><rect x="1" y="2.5" width="10" height="7" fill="none" stroke="var(--orange)" stroke-width="1.2"/><path d="M1 3l5 3.5L11 3" fill="none" stroke="var(--orange)" stroke-width="1.2"/></svg>info@veloriainsurance.com</li>
      <li><svg viewBox="0 0 12 12"><circle cx="6" cy="6" r="4.8" fill="none" stroke="var(--orange)" stroke-width="1.1"/><ellipse cx="6" cy="6" rx="2" ry="4.8" fill="none" stroke="var(--orange)" stroke-width="1"/><path d="M1.2 6h9.6" stroke="var(--orange)" stroke-width="1"/></svg>www.veloriainsurance.com</li>
    </ul>
  </div>
  <div class="feature-block"></div>
  <div class="band-orange"></div>
  <div class="band-blue"></div>
</section>

</body>
</html>
```